Business card for Chiropractic clinics needs reworked / redesigned

The business card in attachment was designed 10 years ago. It is in need of an update.
We have 2 clinics:
VELDHOVE KLINIEK & VELDHOVE KLINIEK NOORD
Only one address needs to be on the card for doctors that only work in one clinic and two addresses need to be on the card for the doctors that work in both clinics.

Target Market(s)

patients/referrers

Industry/Entity Type

Medical

Contact Information for Business Card

Logo (in full or zoomed-in)
Clinic Name
Doctor name and title
clinic address, website, tel, email

Font styles to use
Sans Serif

Colors

Designer to choose colors to be used in the design.

Requirements
Must have
• Good contrast/readability
• We like modern minimalistic designs
• The Bcard needs to project our very high standard of proficiency/professionalism
Should not have
• Not curly
• Not to much colours

```html
<!DOCTYPE html>
<html lang="nl">
<head>
<meta charset="utf-8">
<title>Visitekaartje – Veldhove Kliniek Noord</title>
<link rel="stylesheet" href="https://fonts.googleapis.com/css2?family=Barlow+Condensed:wght@600&family=Work+Sans:wght@400&display=swap">
<style>
  :root {
    --page-bg: #e9e4dc;
    --card-dark: #1b2a2a;
    --card-mid: #243534;
    --card-edge: #2f4140;
    --ink: #d8c9b2;
    --ink-soft: #c4b59e;
  }
  * { margin: 0; padding: 0; box-sizing: border-box; }
  html, body {
    width: 1200px;
    height: 1047px;
    overflow: hidden;
    background: var(--page-bg);
  }
  .business-card {
    position: absolute;
    left: 130px;
    top: 267px;
    width: 940px;
    height: 513px;
    border-radius: 22px;
    background: linear-gradient(100deg, var(--card-edge) 0%, var(--card-mid) 30%, var(--card-dark) 65%, var(--card-mid) 100%);
    color: var(--ink);
    font-family: "Work Sans", sans-serif;
  }
  .doctor-name {
    position: absolute;
    left: 63px;
    top: 98px;
    font-family: "Barlow Condensed", sans-serif;
    font-weight: 600;
    font-size: 40px;
    letter-spacing: 0.5px;
    line-height: 1;
  }
  .doctor-title {
    position: absolute;
    left: 63px;
    top: 142px;
    font-size: 21px;
    color: var(--ink-soft);
    letter-spacing: 0.5px;
  }
  .clinic-block {
    position: absolute;
    left: 63px;
    top: 212px;
    font-size: 22px;
    line-height: 31px;
  }
  .clinic-name { letter-spacing: 0.8px; }
  .contact-list {
    position: absolute;
    left: 63px;
    top: 308px;
    list-style: none;
    font-size: 21px;
    line-height: 29px;
    letter-spacing: 0.4px;
  }
  .contact-list li { display: flex; align-items: center; gap: 10px; }
  .contact-icon { width: 15px; height: 15px; flex: none; }
  .brand-mark {
    position: absolute;
    right: 70px;
    top: 200px;
    display: flex;
    align-items: center;
    gap: 14px;
    font-size: 24px;
    line-height: 32px;
    letter-spacing: 1px;
    text-align: left;
  }
  .brand-dot {
    width: 16px;
    height: 16px;
    border-radius: 50%;
    background: var(--ink);
    flex: none;
  }
</style>
</head>
<body>
  <main class="business-card">
    <h1 class="doctor-name">MAARTEN VERHOEVEN</h1>
    <p class="doctor-title">chiropractor</p>

    <div class="clinic-block">
      <p class="clinic-name">VELDHOVE KLINIEK NOORD</p>
      <p class="clinic-address">Lindenlaan 41</p>
    </div>

    <ul class="contact-list">
      <li>
        <svg class="contact-icon" viewBox="0 0 16 16" aria-hidden="true"><path fill="var(--ink)" d="M3.5 1.5l2.5 0 1 3.5-1.8 1.2a8 8 0 0 0 4.6 4.6L11 9l3.5 1v2.5c0 1-1 2-2 2C6.5 14.5 1.5 9.5 1.5 3.5c0-1 1-2 2-2z"/></svg>
        09 555 01 27
      </li>
      <li>
        <svg class="contact-icon" viewBox="0 0 16 16" aria-hidden="true"><rect x="1.5" y="3.5" width="13" height="9" rx="1" fill="none" stroke="var(--ink)" stroke-width="1.5"/><path d="M2 4l6 5 6-5" fill="none" stroke="var(--ink)" stroke-width="1.5"/></svg>
        info@veldhovekliniek.be
      </li>
      <li>
        <svg class="contact-icon" viewBox="0 0 16 16" aria-hidden="true"><g fill="none" stroke="var(--ink)" stroke-width="1.3"><circle cx="8" cy="8" r="6.5"/><ellipse cx="8" cy="8" rx="3" ry="6.5"/><path d="M1.5 8h13M2.5 4.8h11M2.5 11.2h11"/></g></svg>
        www.veldhovekliniek.be
      </li>
    </ul>

    <div class="brand-mark">
      <span class="brand-dot"></span>
      <span class="brand-name">VELDHOVE<br>KLINIEK</span>
    </div>
  </main>
</body>
</html>
```